Business card design for a engineering company

I need a double sided business card design for my company "Verdmont Flow Solutions". The card will be used in Malaysia. Sleek and professional, with a little design flare to it.
Information to showcase:
1. Company logo
2. Name, title, phone, email address, website address
3. our products "Pumping technology, Valve & actuation, Air Moving Technology
Example:
Ravi Tanaka
Business manager
ravi.tanaka@verdmont-example.com
www.verdmont-example.com.my
- Pumping technology
- Valve & actuation
- Air moving technology
Target Market(s)
engineers, purchasing managers
Industry/Entity Type
Business
Contact Information for Business Card
Ravi Tanaka
Business manager
ravi.tanaka@verdmont-example.com
www.verdmont-example.com.my
- Pumping technology
- Valve & actuation
- Air moving technology
catch phrase : "Solving flow challenges, exceeding expectations"

```html
<!DOCTYPE html>
<html lang="en">
<head>
<meta charset="utf-8">
<title>Verdmont Flow Solutions – Business Card</title>
<link rel="stylesheet" href="https://fonts.googleapis.com/css2?family=Montserrat:wght@400;600;700&display=swap">
<style>
  :root {
    --page-bg: #e9e4da;
    --card-deep: #0b3140;
    --card-mid: #10404f;
    --card-light: #1b5566;
    --ink-white: #ffffff;
    --ink-soft: #c9d8dd;
    --accent-yellow: #f2c21b;
    --rule: rgba(255, 255, 255, 0.45);
  }
  * { box-sizing: border-box; margin: 0; padding: 0; }
  html, body {
    width: 1200px;
    height: 802px;
    overflow: hidden;
    background: var(--page-bg);
    font-family: "Montserrat", Arial, sans-serif;
  }
  .card-set {
    width: 1200px;
    height: 802px;
    display: flex;
    align-items: center;
    justify-content: center;
    gap: 56px;
  }
  .card {
    position: relative;
    width: 532px;
    height: 304px;
    border-radius: 22px;
    overflow: hidden;
    color: var(--ink-white);
    background: linear-gradient(135deg, var(--card-light) 0%, var(--card-mid) 35%, var(--card-deep) 100%);
    box-shadow: 0 6px 18px rgba(0, 0, 0, 0.22);
  }

  /* Wordmark */
  .wordmark {
    position: absolute;
    display: flex;
    align-items: center;
    gap: 12px;
    font-weight: 700;
    color: var(--ink-white);
  }
  .wordmark-square {
    width: 46px;
    height: 46px;
    background: var(--ink-white);
    border-radius: 4px;
    flex: none;
  }
  .wordmark-text { display: flex; flex-direction: column; line-height: 1; }
  .wordmark-name { font-size: 38px; letter-spacing: 1px; }
  .wordmark-sub { font-size: 11px; letter-spacing: 6.2px; margin-top: 4px; }

  /* Front */
  .card-front .wordmark { left: 104px; top: 112px; }
  .front-website {
    position: absolute;
    left: 34px;
    bottom: 26px;
    font-size: 12px;
    font-weight: 600;
    color: var(--ink-soft);
  }

  /* Back */
  .card-back .wordmark { right: 30px; top: 34px; }
  .contact-person {
    position: absolute;
    right: 30px;
    top: 106px;
    text-align: right;
  }
  .person-name {
    font-size: 20px;
    font-weight: 700;
    color: var(--accent-yellow);
  }
  .person-title {
    font-size: 12px;
    color: var(--ink-soft);
    margin-top: 2px;
  }
  .rule-top {
    position: absolute;
    right: 30px;
    top: 158px;
    width: 230px;
    height: 1px;
    background: var(--rule);
  }
  .product-list {
    position: absolute;
    right: 30px;
    top: 168px;
    list-style: none;
    text-align: right;
    font-size: 12.5px;
    line-height: 1.35;
    color: var(--ink-soft);
  }
  .rule-bottom {
    position: absolute;
    left: 30px;
    top: 214px;
    width: 250px;
    height: 1px;
    background: var(--rule);
  }
  .contact-list {
    position: absolute;
    left: 30px;
    top: 222px;
    list-style: none;
    font-size: 12px;
    line-height: 1.4;
    color: var(--ink-soft);
  }
  .contact-list li { display: flex; align-items: center; gap: 8px; }
  .contact-icon { width: 10px; height: 10px; flex: none; fill: var(--accent-yellow); }
</style>
</head>
<body>
<main class="card-set">

  <section class="card card-front" aria-label="Card front">
    <div class="wordmark">
      <span class="wordmark-square"></span>
      <span class="wordmark-text">
        <span class="wordmark-name">VERDMONT</span>
        <span class="wordmark-sub">FLOW SOLUTIONS</span>
      </span>
    </div>
    <p class="front-website">www.verdmont-example.com.my</p>
  </section>

  <section class="card card-back" aria-label="Card back">
    <div class="wordmark">
      <span class="wordmark-square"></span>
      <span class="wordmark-text">
        <span class="wordmark-name">VERDMONT</span>
        <span class="wordmark-sub">FLOW SOLUTIONS</span>
      </span>
    </div>

    <div class="contact-person">
      <p class="person-name">Ravi Tanaka</p>
      <p class="person-title">Business Manager</p>
    </div>
    <div class="rule-top"></div>
    <ul class="product-list">
      <li>Pumping technology</li>
      <li>Valve &amp; actuation</li>
      <li>Air moving technology</li>
    </ul>

    <div class="rule-bottom"></div>
    <ul class="contact-list">
      <li>
        <svg class="contact-icon" viewBox="0 0 10 10" aria-hidden="true"><path d="M1 3 Q5 0 9 3 L8 4.5 L6.5 3.8 L6.5 3 Q5 2.5 3.5 3 L3.5 3.8 L2 4.5 Z M2 5 H8 V9 H2 Z"/></svg>
        <span>xxx.xxxxx.xx</span>
      </li>
      <li>
        <svg class="contact-icon" viewBox="0 0 10 10" aria-hidden="true"><path d="M0.5 2 H9.5 V8 H0.5 Z M1 2.5 L5 5.5 L9 2.5" stroke="#0b3140" stroke-width="0.8"/></svg>
        <span>ravi.tanaka@verdmont-example.com</span>
      </li>
      <li>
        <svg class="contact-icon" viewBox="0 0 10 10" aria-hidden="true"><circle cx="5" cy="5" r="4.5"/><path d="M0.5 5 H9.5 M5 0.5 V9.5" stroke="#0b3140" stroke-width="0.8"/></svg>
        <span>www.verdmont-example.com.my</span>
      </li>
    </ul>
  </section>

</main>
</body>
</html>
```